Business Card Design Project

Professional business cards for law firm - a rough example of what we are looking for is attached. The logo, colour and styling of the name are all new and dont need to be changed. We need layout for front and back. We are looking for some imaginative layout of info. We are a young vibrant firm and not too conservative and are not adverse to something quite different.
Updates

Thank you for all the submissions.  We have been blown away with the quality of your work.  Our management team will be meeting later in the week to make our decision.  Again, thanks for the fabulous work.

Industry/Entity Type

Conservative

Requirements
Must have
• Logo and name as in attached example (colour and font)
Should not have
• Scales of Justice

```html
<!DOCTYPE html>
<html lang="en">
<head>
<meta charset="utf-8">
<title>Ridgeway Lane Legal – Business Cards</title>
<link href="https://fonts.googleapis.com/css2?family=Open+Sans:wght@600&family=Arimo:ital,wght@0,400;0,700;1,700&display=swap" rel="stylesheet">
<style>
  :root {
    --stage: #d6d6d6;
    --card: #ffffff;
    --green: #8dc82a;
    --green-text: #7cb82f;
    --ink: #3a3a3a;
    --muted: #6b6b6b;
    --ring: #7a7a7a;
  }
  * { box-sizing: border-box; margin: 0; padding: 0; }
  html, body { width: 1200px; height: 900px; overflow: hidden; }
  body {
    background: var(--stage);
    position: relative;
    font-family: "Arimo", Arial, sans-serif;
  }
  .card {
    position: absolute;
    width: 640px;
    height: 380px;
    background: var(--card);
    border-radius: 12px;
    overflow: hidden;
    box-shadow: 0 6px 14px rgba(0,0,0,0.25);
  }
  /* Front */
  .card-front { left: 130px; top: 40px; }
  .band { position: absolute; left: 0; right: 0; background: var(--green); }
  .band-top { top: 0; height: 70px; }
  .band-bottom { bottom: 0; height: 72px; }
  .front-brand {
    position: absolute;
    left: 60px; top: 110px;
    display: flex; align-items: center; gap: 44px;
  }
  .brand-mark {
    width: 150px; height: 150px;
    border-radius: 50%;
    border: 4px solid var(--ring);
  }
  .brand-name {
    font-family: "Open Sans", Arial, sans-serif;
    font-weight: 600;
    color: var(--green-text);
    line-height: 1;
  }
  .brand-name .line-main { display: block; font-size: 52px; letter-spacing: -0.5px; }
  .brand-name .line-sub { display: block; font-size: 28px; letter-spacing: 5px; margin-top: 8px; text-align: center; }

  /* Back */
  .card-back { left: 450px; top: 475px; }
  .contact { position: absolute; left: 48px; top: 38px; }
  .person-name { color: var(--green-text); font-weight: 700; font-size: 20px; }
  .person-role { color: var(--green-text); font-weight: 700; font-size: 15px; margin-top: 2px; }
  .details { margin-top: 24px; color: var(--ink); font-size: 13.5px; line-height: 1.3; list-style: none; }
  .back-mark {
    position: absolute; right: 58px; top: 40px;
    width: 170px; height: 170px;
    border-radius: 50%;
    border: 4px solid var(--green);
  }
  .services {
    position: absolute; left: 110px; top: 232px;
    display: grid; grid-template-columns: 230px 200px;
    list-style: none;
    color: var(--muted);
    font-weight: 700; font-style: italic; font-size: 16px; line-height: 1.3;
  }
  .services ul { list-style: none; }
  .services ul + ul { padding-top: 16px; }
  .tagline {
    position: absolute; left: 0; right: 0; bottom: 0; height: 46px;
    background: var(--green);
    color: #fff; font-size: 19px;
    display: flex; align-items: center; justify-content: center;
  }
</style>
</head>
<body>
  <section class="card card-front" aria-label="Card front">
    <div class="band band-top"></div>
    <div class="front-brand">
      <div class="brand-mark"></div>
      <div class="brand-name">
        <span class="line-main">Ridgeway Lane</span>
        <span class="line-sub">LEGAL</span>
      </div>
    </div>
    <div class="band band-bottom"></div>
  </section>

  <section class="card card-back" aria-label="Card back">
    <div class="contact">
      <h1 class="person-name">Clara Whitfield LLB BA</h1>
      <p class="person-role">Solicitor</p>
      <ul class="details">
        <li>4/27 Harcourt Street, Northvale WA 6100</li>
        <li>PO Box 512, Northvale WA 6900</li>
        <li>T: 9000 1234, 9000 5678</li>
        <li>F: 9000 9012</li>
        <li>E: reception@ridgewaylanelegal.com.au</li>
      </ul>
    </div>
    <div class="back-mark"></div>
    <div class="services">
      <ul>
        <li>Family</li>
        <li>Restraining Orders</li>
        <li>Probate/Wills</li>
        <li>Dividing Fences</li>
      </ul>
      <ul>
        <li>Traffic</li>
        <li>Criminal</li>
        <li>Debt Recovery</li>
        <li>Financial Agreements</li>
      </ul>
    </div>
    <p class="tagline">helping you find the way forward</p>
  </section>
</body>
</html>
```